Instagram ad design required

For an IT system house, we need an ad design for a job recruiting campaign on Instagram. A great engaging advertisement is required that encourages potential applicants to click on the ad. The recruiting funnel already exists, only an Instagram ad image should be designed. Follow-up orders for further campaigns as well as Facebook and LinkedIn are possible.
The design of the IT system house Varnholt serves as a design inspiration: www.varnholt.com
The customer should be perceived as a great, modern employer. The target group are young IT technicians who want to work in a cool and modern company. For example, the topic could be IT Super Hero wanted with corresponding graphic content.
Target Market(s)
IT system technician
Industry/Entity Type
Informatik
Other font styles liked:
- PT Sans
Look and feel
Each slider illustrates characteristics of the customer's brand and the style your logo design should communicate.

```html
<!DOCTYPE html>
<html lang="en">
<head>
<meta charset="utf-8">
<title>Varnholt – We Are Hiring</title>
<link href="https://fonts.googleapis.com/css2?family=Righteous&family=Titan+One&family=Poppins:ital,wght@0,400;0,600;0,700;0,800;1,400&display=swap" rel="stylesheet">
<style>
  :root {
    --green: #2e9a5e;
    --ink: #3a3a3c;
    --black: #161616;
    --paper: #eef0ef;
    --white: #ffffff;
  }
  * { margin: 0; padding: 0; box-sizing: border-box; }
  html, body { width: 1200px; height: 1200px; overflow: hidden; }
  body { background: var(--paper); font-family: "Poppins", sans-serif; color: var(--black); }

  .ad {
    position: relative; width: 1200px; height: 1200px; overflow: hidden;
    background:
      radial-gradient(ellipse at 20% 30%, rgba(255,255,255,.7), transparent 60%),
      radial-gradient(ellipse at 75% 85%, rgba(210,214,212,.5), transparent 55%),
      var(--paper);
  }

  .dots { position: absolute; left: 56px; top: 53px; display: grid; grid-template-columns: repeat(5, 7px); column-gap: 19px; row-gap: 18px; }
  .dots span { width: 7px; height: 7px; border-radius: 2px; background: var(--green); }

  .brand {
    position: absolute; left: 890px; top: 122px; display: flex; align-items: center; gap: 12px;
  }
  .brand-mark { width: 22px; height: 22px; background: var(--green); }
  .brand-name { font-family: "Poppins", sans-serif; font-weight: 700; font-size: 32px; line-height: 40px; color: var(--black); }

  .headline { position: absolute; left: 56px; top: 108px; }
  .headline .lead, .headline .tail {
    font-family: "Righteous", sans-serif; color: var(--ink); text-transform: uppercase;
    text-shadow: 0 0 6px var(--white), 0 0 2px var(--white), 2px 3px 6px rgba(0,0,0,.25);
  }
  .headline .lead { font-size: 74px; line-height: 80px; letter-spacing: 3px; }
  .headline .big {
    font-family: "Titan One", sans-serif; font-size: 168px; line-height: 150px; color: var(--green);
    letter-spacing: -2px; margin-top: 4px; margin-left: -4px;
    text-shadow: 0 0 8px var(--white), 0 0 3px var(--white), 3px 4px 8px rgba(0,0,0,.2);
  }
  .headline .tail { font-size: 68px; line-height: 74px; letter-spacing: 3px; margin-top: 6px; }

  .intro { position: absolute; left: 56px; top: 432px; width: 540px; font-style: italic; font-size: 20.5px; line-height: 30px; }

  .req-title { position: absolute; left: 87px; top: 558px; font-weight: 700; font-size: 42px; }
  .req-list { position: absolute; left: 87px; top: 638px; list-style: none; }
  .req-item { position: relative; padding-left: 41px; margin-bottom: 20px; }
  .req-item svg { position: absolute; left: 0; top: 4px; }
  .req-item h3 { font-weight: 800; font-size: 24px; line-height: 30px; text-transform: uppercase; }
  .req-item p { font-style: italic; font-size: 16.5px; line-height: 21px; margin-top: 2px; }

  .cv-title { position: absolute; left: 59px; top: 946px; font-weight: 800; font-size: 33px; letter-spacing: 1.5px; }
  .cv-mail {
    position: absolute; left: 58px; top: 1000px; width: 504px; height: 68px; border-radius: 14px;
    background: var(--green); display: flex; align-items: center; padding-left: 19px;
    box-shadow: 0 0 0 6px rgba(255,255,255,.8), 0 6px 14px rgba(0,0,0,.12);
  }
  .cv-mail .icon { width: 44px; height: 44px; border-radius: 50%; background: var(--white); display: flex; align-items: center; justify-content: center; }
  .cv-mail span { margin-left: 17px; color: var(--white); font-size: 36px; }
  .cv-note { position: absolute; left: 59px; top: 1082px; width: 420px; font-size: 15px; line-height: 20px; }

  .photo {
    position: absolute; left: 0; top: 0; width: 1200px; height: 1200px;
    background: linear-gradient(115deg, #c8b99a 0%, #6f8a45 30%, #4f6b2e 50%, #d98a1c 72%, #e2941f 82%, #7d9ab8 100%);
    clip-path: polygon(741px 199px, 1200px 199px, 1200px 960px, 578px 960px);
  }

  .contact {
    position: absolute; left: 785px; top: 996px; width: 440px; height: 144px; border-radius: 24px;
    background: var(--paper); box-shadow: 0 4px 14px rgba(0,0,0,.18);
  }
  .contact-row { position: absolute; left: 28px; display: flex; align-items: center; }
  .contact-row .label { font-size: 13.5px; line-height: 16px; }
  .contact-row .label.small { font-size: 12px; }
  .contact-row .value { font-weight: 700; font-size: 22px; line-height: 26px; }
  .contact-row .text { margin-left: 22px; }
</style>
</head>
<body>
<main class="ad">
  <div class="dots"><span></span><span></span><span></span><span></span><span></span><span></span><span></span><span></span><span></span><span></span></div>

  <div class="brand"><span class="brand-mark"></span><span class="brand-name">Varnholt</span></div>

  <h1 class="headline">
    <div class="lead">We Are</div>
    <div class="big">HIRING</div>
    <div class="tail">Join Our Team</div>
  </h1>

  <p class="intro">Lorem ipsum dolor sit amet, consectetuer<br>adipiscing elit, sed diam nonummy nibh euismod<br>tincidunt ut laoreet dolore magna aliqua.</p>

  <h2 class="req-title">Requirement :</h2>
  <ul class="req-list">
    <li class="req-item">
      <svg width="26" height="22" viewBox="0 0 26 22"><circle cx="10" cy="12" r="8" fill="none" stroke="#161616" stroke-width="3"/><path d="M6 12l4 4L23 3" fill="none" stroke="#161616" stroke-width="3.2" stroke-linecap="round" stroke-linejoin="round"/></svg>
      <h3>Lorem ipsum dolor sit amet.</h3>
      <p>Lorem ipsum dolor sit amet,<br>consectetuer adipiscing elit, sed diam</p>
    </li>
    <li class="req-item">
      <svg width="26" height="22" viewBox="0 0 26 22"><circle cx="10" cy="12" r="8" fill="none" stroke="#161616" stroke-width="3"/><path d="M6 12l4 4L23 3" fill="none" stroke="#161616" stroke-width="3.2" stroke-linecap="round" stroke-linejoin="round"/></svg>
      <h3>Lorem ipsum dolor.</h3>
      <p>Lorem ipsum dolor sit amet, consectetuer<br>adipiscing.</p>
    </li>
    <li class="req-item">
      <svg width="26" height="22" viewBox="0 0 26 22"><circle cx="10" cy="12" r="8" fill="none" stroke="#161616" stroke-width="3"/><path d="M6 12l4 4L23 3" fill="none" stroke="#161616" stroke-width="3.2" stroke-linecap="round" stroke-linejoin="round"/></svg>
      <h3>Lorem ipsum.</h3>
      <p>Lorem ipsum dolor sit amet,<br>consectetuer adipiscing elit, sed diam</p>
    </li>
  </ul>

  <div class="cv-title">SUBMIT YOUR CV</div>
  <div class="cv-mail">
    <div class="icon"><svg width="26" height="20" viewBox="0 0 26 20"><rect x="2" y="2" width="22" height="16" rx="3" fill="none" stroke="#2e9a5e" stroke-width="2.5"/><path d="M3 4l10 8 10-8M3 17l7-6M23 17l-7-6" fill="none" stroke="#2e9a5e" stroke-width="2.2"/></svg></div>
    <span>yourname@email.com</span>
  </div>
  <p class="cv-note">Lorem ipsum dolor sit amet, consectetuer adipiscing elit, sed diam nonummy nibh euismod tincidunt ut laoreet dolore magna aliqua.</p>

  <div class="photo" role="img" aria-label="Photo of a smiling young employee in an orange blouse working on a laptop among green plants"></div>

  <aside class="contact">
    <div class="contact-row" style="top:20px">
      <svg width="42" height="42" viewBox="0 0 42 42"><circle cx="21" cy="21" r="20" fill="#161616"/><g fill="none" stroke="#fff" stroke-width="1.8"><circle cx="21" cy="21" r="13"/><ellipse cx="21" cy="21" rx="6" ry="13"/><path d="M8 21h26M10 14h22M10 28h22M21 8v26"/></g></svg>
      <div class="text"><div class="label">Visit our website</div><div class="value">www.website.com</div></div>
    </div>
    <div class="contact-row" style="top:82px">
      <svg width="42" height="42" viewBox="0 0 42 42"><circle cx="21" cy="21" r="20" fill="#161616"/><path d="M15 11c-2 1-3 3-2 6 2 6 6 11 12 14 3 1 5 0 6-2l-4-4-3 2c-3-2-5-5-7-8l2-3z" fill="#fff"/></svg>
      <div class="text"><div class="label small">More information call us</div><div class="value">+00 123 456 789</div></div>
    </div>
  </aside>
</main>
</body>
</html>
```